Dog treat bakery needs updated bag labels

We're a small-batch dog treat bakery and would like to update our front bag labels to 1) differentiate our line of products and 2) to stand out on shelves. We believe all dogs deserve to eat clean, healthy foods. That's why we bake low-calorie, clean treats made with simple, premium ingredients like teff, amaranth, and sorghum flours and 100% blueberry, carrot, and purple sweet potato. All our treats are made gluten free without preservatives, artificial flavors, soy, corn, wheat, or eggs. Clean treats, happy dogs!

see uploaded files

```html
<!DOCTYPE html>
<html lang="en">
<head>
<meta charset="utf-8">
<title>Maple Hollow – Rosie's Bites label</title>
<link rel="stylesheet" href="https://fonts.googleapis.com/css2?family=Archivo+Black&family=Fira+Sans+Condensed:wght@700&family=Fira+Sans:ital,wght@1,300;1,600&display=swap">
<style>
  :root {
    --ink: #231a1a;
    --paper: #ffffff;
    --aqua: #b1e6e1;
    --fur: #c8692a;
    --fur-mid: #d9874a;
    --fur-light: #f3e6d4;
  }
  html, body { margin: 0; padding: 0; overflow: hidden; }
  .label {
    position: relative;
    width: 1200px;
    height: 800px;
    overflow: hidden;
    background: var(--aqua);
    color: var(--ink);
  }
  .top-band {
    position: absolute;
    left: 0; top: 0;
    width: 1200px; height: 497px;
    background: var(--ink);
  }
  .brand-name {
    position: absolute;
    left: 0; top: 24px;
    width: 1200px;
    margin: 0;
    text-align: center;
    font-family: "Fira Sans Condensed", sans-serif;
    font-weight: 700;
    font-size: 136px;
    line-height: 1;
    letter-spacing: 0;
    color: var(--paper);
    white-space: nowrap;
  }
  .claim {
    position: absolute;
    display: flex;
    align-items: center;
    justify-content: center;
    background: var(--paper);
    border-radius: 60px;
    font-family: "Fira Sans Condensed", sans-serif;
    font-weight: 700;
    color: var(--ink);
    white-space: nowrap;
  }
  .claim--free-from {
    left: 161px; top: 200px;
    width: 879px; height: 103px;
    font-size: 56px;
  }
  .claim--ingredients {
    left: 22px; top: 340px;
    width: 1157px; height: 104px;
    font-size: 48px;
    letter-spacing: 1px;
  }
  .product-name {
    position: absolute;
    left: 28px; top: 515px;
    margin: 0;
    font-family: "Archivo Black", sans-serif;
    font-size: 108px;
    line-height: 1;
    letter-spacing: -3px;
    white-space: nowrap;
  }
  .detail {
    position: absolute;
    right: 414px;
    margin: 0;
    text-align: right;
    font-family: "Fira Sans", sans-serif;
    font-style: italic;
    line-height: 1;
    white-space: nowrap;
  }
  .product-type { top: 640px; font-weight: 600; font-size: 56px; }
  .calories { top: 706px; font-weight: 300; font-size: 47px; }
  .net-weight { top: 750px; font-weight: 300; font-size: 41px; letter-spacing: -1px; }
  .mascot {
    position: absolute;
    left: 833px; top: 441px;
    width: 354px; height: 347px;
  }
</style>
</head>
<body>
  <div class="label">
    <div class="top-band"></div>
    <h1 class="brand-name">Maple Hollow</h1>
    <div class="claim claim--free-from">No Soy, Corn, Wheat, Eggs or Dairy</div>
    <div class="claim claim--ingredients">Made with Ancient Grains and Grass-Fed Beef Liver</div>

    <h2 class="product-name">Rosie's Bites</h2>
    <p class="detail product-type">Gluten Free - Dog Treats</p>
    <p class="detail calories">10 Calories each</p>
    <p class="detail net-weight">NET WT 4 OZ (113g)</p>

    <svg class="mascot" viewBox="0 0 354 347" role="img" aria-label="Illustration of a sitting corgi with its tongue out">
      <defs>
        <linearGradient id="mascot-tone" x1="0" y1="0" x2="1" y2="1">
          <stop offset="0" stop-color="#c8692a"/>
          <stop offset="0.55" stop-color="#d9874a"/>
          <stop offset="1" stop-color="#f3e6d4"/>
        </linearGradient>
      </defs>
      <rect x="0" y="0" width="354" height="347" rx="40" fill="url(#mascot-tone)"/>
    </svg>
  </div>
</body>
</html>
```